Accommodation business card design

We need a business card designed for our long-term accommodation business based in Australia. The business card must match the style of the attached letterhead and logo. The same contact details that are on the letterhead will also go on the card except that the card must list the contact details in the following order:phone, email, home address, ABN.

The card will be printed on .76mm white pvc plastic (same as credit cards), printed both sides and will be silver foil stamped on at least one side (preferably 2 sides) The design template is attached, but please go to www.zt.com.au for more specs.

The only other addition the card will be my name: Malcolm Darby

```html
<!DOCTYPE html>
<html lang="en">
<head>
<meta charset="utf-8">
<title>Ridgeline Lodging – Business Card</title>
<link rel="stylesheet" href="https://fonts.googleapis.com/css2?family=Open+Sans:wght@400;600;800&display=swap">
<style>
  :root {
    --maroon: #6e1a3c;
    --brown: #8a4a3e;
    --ink: #2a2a2a;
    --card: #ffffff;
    --backdrop: #e4e4ea;
  }
  * { margin: 0; padding: 0; box-sizing: border-box; }
  html, body { width: 1200px; height: 987px; overflow: hidden; }
  body {
    background: var(--backdrop);
    font-family: "Open Sans", Arial, sans-serif;
    position: relative;
  }
  .card {
    position: absolute;
    width: 560px;
    height: 353px;
    background: var(--card);
    border-radius: 28px;
    overflow: hidden;
    box-shadow: 0 6px 18px rgba(0,0,0,0.12);
  }
  .card-back { left: 600px; top: 110px; }
  .card-front { left: 40px; top: 520px; }

  .brand {
    position: absolute;
    display: flex;
    align-items: center;
    gap: 16px;
  }
  .brand-square {
    width: 74px; height: 74px;
    background: var(--maroon);
    border-radius: 12px;
    flex: none;
  }
  .brand-name {
    color: var(--maroon);
    font-weight: 800;
    font-size: 34px;
    line-height: 1.0;
    text-transform: uppercase;
    letter-spacing: 0.5px;
  }
  .card-back .brand { left: 110px; top: 110px; }
  .web {
    position: absolute;
    left: 0; right: 0; top: 230px;
    text-align: center;
    font-size: 17px;
    letter-spacing: 5px;
    color: var(--ink);
  }

  .front-art { position: absolute; inset: 0; }
  .card-front .brand { left: 190px; top: 40px; }
  .card-front .brand-square { width: 62px; height: 62px; }
  .card-front .brand-name { font-size: 29px; }
  .holder {
    position: absolute;
    left: 190px; top: 140px;
    color: var(--brown);
    font-weight: 600;
    font-size: 21px;
  }
  .contacts {
    position: absolute;
    left: 190px; top: 182px;
    list-style: none;
    font-size: 14.5px;
    color: var(--ink);
    line-height: 25px;
  }
  .contacts li { display: flex; align-items: center; gap: 8px; }
  .contacts svg { width: 14px; height: 14px; fill: var(--brown); flex: none; }
  .contacts .abn { padding-left: 22px; }
</style>
</head>
<body>

<section class="card card-back">
  <div class="brand">
    <div class="brand-square"></div>
    <div class="brand-name">Ridgeline<br>Lodging</div>
  </div>
  <p class="web">www.zt.com.au</p>
</section>

<section class="card card-front">
  <svg class="front-art" viewBox="0 0 560 353" aria-hidden="true">
    <path d="M0 0 H185 C110 60 50 180 30 353 H0 Z" fill="var(--brown)"/>
    <path d="M160 60 C95 120 60 230 52 353 H30 C48 220 85 120 160 60 Z" fill="var(--maroon)"/>
    <path d="M52 353 C60 230 95 120 160 60 C120 110 95 220 92 353 Z" fill="var(--maroon)"/>
  </svg>
  <div class="brand">
    <div class="brand-square"></div>
    <div class="brand-name">Ridgeline<br>Lodging</div>
  </div>
  <p class="holder">Malcolm Darby</p>
  <ul class="contacts">
    <li><svg viewBox="0 0 24 24"><path d="M6.6 10.8a15 15 0 0 0 6.6 6.6l2.2-2.2a1 1 0 0 1 1-.25 11.4 11.4 0 0 0 3.6.57 1 1 0 0 1 1 1V20a1 1 0 0 1-1 1A17 17 0 0 1 3 4a1 1 0 0 1 1-1h3.5a1 1 0 0 1 1 1c0 1.25.2 2.45.57 3.57a1 1 0 0 1-.25 1z"/></svg>0412 555 308</li>
    <li><svg viewBox="0 0 24 24"><path d="M2 5h20v14H2z M2 5l10 8 10-8" fill="none" stroke="var(--brown)" stroke-width="2.4"/></svg>malcolmdarby@mail.com</li>
    <li><svg viewBox="0 0 24 24"><path d="M12 2a7 7 0 0 0-7 7c0 5 7 13 7 13s7-8 7-13a7 7 0 0 0-7-7zm0 9.5A2.5 2.5 0 1 1 12 6.5a2.5 2.5 0 0 1 0 5z"/></svg>PO Box 1187, Kirra Mail Centre, QLD 4825</li>
    <li class="abn">ABN 51 807 326 914</li>
  </ul>
</section>

</body>
</html>
```